① 使用イメージは、需要家に訪問して若草新電力を紹介する時に渡す。
② 相手は企業のトップ・総務担当者なので軽すぎない内容がよい。
③ 新電力に切り替えれば安くなることがわかっていても踏み切れない需要家をターゲットにした内容。
④ 両面なので、表は、キャッチコピー~導入効果の全体説明までか、その続きの、ポイント1の電気料金削減事例までぐらいになるのではと考えます。(素人の発想ですが)
⑤ 他社のHP参考: ミズサワ金属工業(www.mizusawa-mk.example.jp/new-power/)
若草新電力(denki.wakakusa-pw.example.jp/deregulatin/)その他新電力のHP参考
裏面最下部に会社名、ロゴマーク、若草新電力㈱正規代理店、住所、電話番号、お見積・気になること等お気軽にお問合せ下さいの文言を入れる。
カナリオのロゴマーク使用・若草新電力㈱のロゴは使用できない・キャッチコピーについては現状のチラシで使用している「若草新電力でお見積りすれば分かる!!」「電気料金はもっと安くなる!!」に拘っていない。
ポイント3を図で説明した資料添付・なぜ安くなるの?の説明した2つの図(見栄え良く加工してほしい)を添付
株式会社カナリオ 〒759-0000 山口県下関市椎野町5-7-3 TEL083-253-2125
A4
両面
シンプル 複雑
単色 カラフル
暗い 明るい
日常 高級
遊び心 厳粛
未来的 伝統的
女性的 男性的
• 高解像度JPG (.jpg)
• イラストレーター形式 (.ai)
未切り替えの需要家の方の声として
① 「新電力の売込電話」にうんざり
② 「新電力にうさんくささ」を感じる
③ 「新電力に変更するメリット」が判らない
信頼できる新電力会社は一体どこか?需要家の迷い・戸惑い・情報不足で打つ手が判らとの声も聞かれます。提案をなかなか聞いてもらえないこともあります。
新電力を選ぶ上で大切なことは
⇒①新電力に一番求められることはコスト削減
② 新電力の実績と将来に渡る信頼性・安心感
③ 新電力変更する手続きの簡便さ
※信頼できる若草電力こそ「コスト削減」の切札 と考えます。
企業活動で重要なこと、それは「経費削減」「損失防止」「売上拡大」と言われております。
削れる「コスト」はいますぐ削ることが、経営者目線で重要なことと考えます。
そういった意味からも、新電力に切替えるタイミングは今と思います。

対象が企業の社長様や総務の管理職と言うことで、落ち着いた中にも、わかりやすく、全体像が、流れるように見ることで意図を理解できる点と、写真から電力の未来が新電力の参入で明るく開けるような予感が感じられたことです。人の動きがない分若干地味ではありますが、我々もこれから新電力を広めたいとの思いが湧いてきました。

今回当選した案以外、どの案も素晴らしく感心しました。
皆さん全員に御礼申し上げます。
次回又機会があれば、皆さんにご参加いただきたいと考えています。
皆さんの今後のご活躍期待しています。
本当にありがとうございました。

```html
<!DOCTYPE html>
<html lang="ja">
<head>
<meta charset="utf-8">
<title>若草新電力 正規代理店 カナリオ ご案内(裏面)</title>
<link href="https://fonts.googleapis.com/css2?family=Noto+Sans+JP:wght@400;500;700;900&family=Roboto+Condensed:wght@700&display=swap" rel="stylesheet">
<style>
:root{
  --red:#d4241c;
  --red-dark:#b01812;
  --pink:#fbe7e5;
  --navy:#1c2d57;
  --blue:#2f5fa8;
  --sky-top:#6f8fb6;
  --sky-bottom:#c9d8ea;
  --ink:#2b2b2b;
  --gray:#e7e7e7;
  --gray-dark:#8a8a8a;
  --paper:#ffffff;
}
*{box-sizing:border-box;margin:0;padding:0}
html,body{width:849px;height:1200px;overflow:hidden;background:var(--paper)}
body{font-family:"Noto Sans JP",sans-serif;color:var(--ink);position:relative;font-size:9px;line-height:1.55}

.hero-band{position:absolute;left:0;top:0;width:849px;height:78px;background:linear-gradient(180deg,var(--sky-top),var(--sky-bottom))}
.tagline{position:absolute;right:18px;top:10px;text-align:right;font-family:"Roboto Condensed",sans-serif;font-weight:700;color:var(--navy);line-height:1}
.tagline .t1{font-size:15px;letter-spacing:2px}
.tagline .t2{font-size:17px}

.left-col{position:absolute;left:12px;top:86px;width:505px}
.right-col{position:absolute;left:530px;top:86px;width:308px}

.point{margin-bottom:10px}
.point-head{display:flex;align-items:center;border-bottom:2px solid var(--red);padding-bottom:3px;margin-bottom:6px}
.point-label{background:var(--red);color:#fff;font-weight:700;font-size:11px;padding:3px 6px 3px 10px;border-radius:3px;display:flex;align-items:center;gap:5px}
.point-num{width:22px;height:22px;border-radius:50%;background:#fff;color:var(--red);font-family:"Roboto Condensed",sans-serif;font-size:17px;display:flex;align-items:center;justify-content:center}
.point-title{color:var(--red);font-weight:900;font-size:17px;margin-left:10px}
.lead{color:var(--red);font-weight:700;font-size:12px;margin-bottom:3px}
.body-text{font-size:8.5px;line-height:1.6;color:#444}

.case{margin-bottom:4px}
.case-name{font-size:9px;font-weight:700}
.case-name span{color:var(--red)}
.case-bar{display:flex;align-items:center;height:20px;margin-top:1px}
.case-from{background:var(--gray);flex:0 0 230px;height:100%;display:flex;align-items:center;padding-left:6px;font-size:9px;color:#777;gap:6px}
.case-from b{font-size:10px;color:#555}
.case-arrow{width:0;height:0;border-top:10px solid transparent;border-bottom:10px solid transparent;border-left:10px solid var(--gray)}
.case-save{flex:1;height:100%;background:var(--pink);margin-left:6px;display:flex;align-items:center;justify-content:flex-end;padding-right:8px;color:var(--red);font-weight:900;font-size:14px}
.case-save small{font-size:10px;margin-left:3px}

.note{display:flex;align-items:center;gap:8px;margin-top:6px}
.note-badge{background:var(--red);color:#fff;font-weight:900;font-size:10px;border-radius:50%;width:38px;height:38px;display:flex;align-items:center;justify-content:center}
.note-text{font-size:9px;color:#444}

.safe-box{display:flex;gap:8px;margin-top:6px;border:1px solid #ddd;padding:6px}
.safe-list{flex:0 0 175px}
.safe-list h4{background:var(--red);color:#fff;font-size:10px;padding:2px 6px;margin-bottom:4px}
.safe-list li{list-style:none;font-size:8.5px;margin-bottom:3px;padding-left:13px;position:relative}
.safe-list li::before{content:"✓";position:absolute;left:0;color:var(--red);font-weight:900}

.agent{position:absolute;left:12px;top:1118px;width:505px;height:70px;display:flex;align-items:center;gap:26px;border-top:1px solid #ccc;padding-top:8px}
.agent-name{font-weight:900;font-size:15px;color:var(--navy);line-height:1.3}
.brand{display:flex;align-items:center;gap:7px;font-weight:900;font-size:20px;color:var(--navy)}
.brand i{width:22px;height:22px;background:var(--navy);display:block}
.brand small{font-size:11px;font-weight:900}

.why-title{font-size:25px;font-weight:900;color:var(--navy);line-height:1.2}
.why-sub{font-size:13px;font-weight:700;color:var(--navy);margin:4px 0 8px;border-bottom:1px solid var(--navy);padding-bottom:4px}
.why-sub em{font-style:normal;color:var(--red)}
.why-text p{font-size:8.5px;line-height:1.65;margin-bottom:5px;color:#444}
.chart-card{border:2px solid var(--navy);border-radius:4px;padding:6px;margin-top:6px;background:#fff}
.chart-card h3{font-size:13px;color:var(--navy);font-weight:900}
.chart-card h3 em{font-style:normal;color:var(--red)}
.chart-cap{font-size:8.5px;color:#444;margin-top:4px}

.contact{position:absolute;left:530px;top:1040px;width:308px}
.contact-note{background:var(--gray);font-size:8.5px;padding:6px 8px;color:#444}
.contact-main{margin-top:6px;display:flex;justify-content:space-between;align-items:flex-end}
.contact-main p{font-size:9px;font-weight:700;color:var(--navy);line-height:1.5}
.tel{font-size:22px;font-weight:900;color:var(--red);line-height:1.1;margin-top:4px}
.address{font-size:8.5px;color:#444}
</style>
</head>
<body>

<div class="hero-band" role="img" aria-label="青空を背景に並ぶ送電鉄塔と送電線の写真"></div>
<div class="tagline"><div class="t1">Trust</div><div class="t2">New Power</div></div>

<main class="left-col">
  <section class="point">
    <div class="point-head"><div class="point-label">ポイント<span class="point-num">1</span></div><div class="point-title">電気料金削減</div></div>
    <p class="lead">電気料金削減の実例をご紹介いたします!</p>
    <div class="case">
      <div class="case-name"><span>実例①:</span> 食品工場様【契約電力389kW】</div>
      <div class="case-bar"><div class="case-from">年間電気料金 <b>21,170,000円 → 19,550,000円</b></div><div class="case-arrow"></div><div class="case-save">1,620,000円<small>(7.7%削減)</small></div></div>
    </div>
    <div class="case">
      <div class="case-name"><span>実例②:</span> 観光ホテル様【契約電力360kW】</div>
      <div class="case-bar"><div class="case-from">年間電気料金 <b>20,440,000円 → 18,320,000円</b></div><div class="case-arrow"></div><div class="case-save">2,120,000円<small>(10.3%削減)</small></div></div>
    </div>
    <div class="case">
      <div class="case-name"><span>実例③:</span> スーパーマーケット様【契約電力460kW】</div>
      <div class="case-bar"><div class="case-from">年間電気料金 <b>30,000,000円 → 28,750,000円</b></div><div class="case-arrow"></div><div class="case-save">1,250,000円<small>(4.1%削減)</small></div></div>
    </div>
    <div class="note"><div class="note-badge">なんと!</div><p class="note-text">御社のご利用状況次第で、こんなに安くなる可能性があります。まずはお気軽にお見積りをご依頼ください。</p></div>
  </section>

  <section class="point">
    <div class="point-head"><div class="point-label">ポイント<span class="point-num">2</span></div><div class="point-title">導入コスト0円</div></div>
    <p class="lead">お見積り、ご相談、ご契約、その他手数料 完全無料!</p>
    <p class="body-text">切り替えにあたって、工事費や初期費用などの負担は一切ありません。これまでの設備や電気メーターはそのままご利用いただけます。コストをかけずに電気料金の削減を始められます。</p>
  </section>

  <section class="point">
    <div class="point-head"><div class="point-label">ポイント<span class="point-num">3</span></div><div class="point-title">変わらない品質と安定供給</div></div>
    <p class="lead">今までと変わらぬ品質で電気をご利用いただけます!</p>
    <p class="body-text">電気は今までと同じ送配電網を通じて届けられるため、停電のしやすさや電気の品質は変わりません。万一の際も地域の送配電事業者が対応いたします。</p>
    <div class="safe-box">
      <div class="safe-list">
        <h4>安心ポイント</h4>
        <ul>
          <li>電気の品質はこれまでと同じ</li>
          <li>送配電網は従来のまま利用</li>
          <li>停電時の対応も変わりません</li>
          <li>工事・設備交換は不要</li>
        </ul>
      </div>
      <svg width="300" height="112" viewBox="0 0 300 112" aria-label="電気が届く仕組みの図">
        <defs><marker id="ah" markerWidth="8" markerHeight="8" refX="6" refY="4" orient="auto"><path d="M0,0 L8,4 L0,8z" fill="#2f5fa8"/></marker></defs>
        <rect x="100" y="4" width="100" height="24" rx="4" fill="#d4241c"/>
        <text x="150" y="20" font-size="10" font-weight="700" fill="#fff" text-anchor="middle">若草新電力</text>
        <rect x="4" y="58" width="76" height="36" rx="4" fill="#e7eef8" stroke="#2f5fa8"/>
        <text x="42" y="80" font-size="10" font-weight="700" fill="#1c2d57" text-anchor="middle">発電所</text>
        <rect x="108" y="58" width="86" height="36" rx="4" fill="#e7eef8" stroke="#2f5fa8"/>
        <text x="151" y="74" font-size="9" font-weight="700" fill="#1c2d57" text-anchor="middle">送配電網</text>
        <text x="151" y="87" font-size="7.5" fill="#1c2d57" text-anchor="middle">(地域の電力会社)</text>
        <rect x="222" y="58" width="74" height="36" rx="4" fill="#fbe7e5" stroke="#d4241c"/>
        <text x="259" y="80" font-size="10" font-weight="700" fill="#d4241c" text-anchor="middle">お客様</text>
        <line x1="82" y1="76" x2="104" y2="76" stroke="#2f5fa8" stroke-width="2" marker-end="url(#ah)"/>
        <line x1="196" y1="76" x2="218" y2="76" stroke="#2f5fa8" stroke-width="2" marker-end="url(#ah)"/>
        <line x1="150" y1="30" x2="150" y2="54" stroke="#d4241c" stroke-width="1.5" stroke-dasharray="3 2"/>
        <text x="156" y="46" font-size="7.5" fill="#d4241c">電力を調達・販売</text>
      </svg>
    </div>
  </section>

  <section class="point">
    <div class="point-head"><div class="point-label">ポイント<span class="point-num">4</span></div><div class="point-title">かんたん手続き</div></div>
    <p class="lead">面倒な手続きは、一切必要ありません!</p>
    <p class="body-text">若草新電力への切り替えは、申込書にご記入いただくだけで完了します。現在の電力会社への解約手続きも当社が代行いたしますので、お客様のお手間はかかりません。切り替え後もこれまで通り電気をご利用いただけます。安心・簡単・スピーディーです。</p>
  </section>
</main>

<footer class="agent">
  <div class="agent-name">若草新電力㈱<br>正規代理店</div>
  <div class="brand"><i></i>カナリオ <small>株式会社カナリオ</small></div>
</footer>

<aside class="right-col">
  <h2 class="why-title">なぜ安くなるの?</h2>
  <p class="why-sub">切り替え後には<em>より安くなる</em>理由</p>
  <div class="why-text">
    <p>電気料金は、基本料金と使用電力量に応じた料金の二つで構成されています。新電力は自社の発電設備や市場からの調達を組み合わせ、効率的に電力を供給しています。</p>
    <p>そのため、従来の電力会社と比べて基本料金の単価を低く設定することができ、使用量が同じでも毎月の電気料金を抑えることが可能です。</p>
    <p>さらに、ピーク需要を踏まえた最適な契約プランをご提案することで、無駄のない電気の使い方を実現します。</p>
  </div>

  <div class="chart-card">
    <h3>「基本料金」の面で<em>安くなる!</em></h3>
    <svg width="292" height="120" viewBox="0 0 292 120" aria-label="月ごとの最大需要電力の推移グラフ">
      <line x1="26" y1="8" x2="26" y2="100" stroke="#555"/>
      <line x1="26" y1="100" x2="286" y2="100" stroke="#555"/>
      <text x="4" y="12" font-size="7" fill="#555">kW</text>
      <line x1="26" y1="30" x2="286" y2="30" stroke="#d4241c" stroke-dasharray="4 3"/>
      <text x="232" y="26" font-size="7.5" fill="#d4241c">契約電力</text>
      <polyline points="36,70 58,62 80,55 102,48 124,34 146,32 168,40 190,52 212,60 234,58 256,50 278,46" fill="none" stroke="#2f5fa8" stroke-width="2"/>
      <circle cx="146" cy="32" r="3" fill="#d4241c"/>
      <text x="150" y="46" font-size="7.5" fill="#1c2d57">最大需要電力</text>
      <text x="36" y="112" font-size="7" fill="#555">4月</text>
      <text x="140" y="112" font-size="7" fill="#555">8月</text>
      <text x="268" y="112" font-size="7" fill="#555">3月</text>
    </svg>
  </div>

  <div class="chart-card">
    <h3>基本料金の比較</h3>
    <svg width="292" height="150" viewBox="0 0 292 150" aria-label="従来の電力会社と若草新電力の料金比較棒グラフ">
      <line x1="20" y1="130" x2="286" y2="130" stroke="#555"/>
      <rect x="50" y="30" width="70" height="60" fill="#8a8a8a"/>
      <rect x="50" y="90" width="70" height="40" fill="#c4c4c4"/>
      <rect x="170" y="50" width="70" height="40" fill="#d4241c"/>
      <rect x="170" y="90" width="70" height="40" fill="#f2a9a4"/>
      <text x="85" y="64" font-size="8" fill="#fff" text-anchor="middle">基本料金</text>
      <text x="85" y="114" font-size="8" fill="#333" text-anchor="middle">電力量料金</text>
      <text x="205" y="74" font-size="8" fill="#fff" text-anchor="middle">基本料金</text>
      <text x="205" y="114" font-size="8" fill="#333" text-anchor="middle">電力量料金</text>
      <text x="85" y="143" font-size="8.5" font-weight="700" fill="#333" text-anchor="middle">従来の電力会社</text>
      <text x="205" y="143" font-size="8.5" font-weight="700" fill="#d4241c" text-anchor="middle">若草新電力</text>
      <line x1="122" y1="30" x2="168" y2="50" stroke="#d4241c" stroke-dasharray="3 2"/>
      <text x="205" y="42" font-size="9" font-weight="900" fill="#d4241c" text-anchor="middle">削減!</text>
    </svg>
    <p class="chart-cap">基本料金の単価が下がることで、年間の電気料金が大きく削減できます。</p>
  </div>
</aside>

<section class="contact">
  <p class="contact-note">まずは現在の使用状況等を拝見して、最適なプランをご提案いたします。</p>
  <div class="contact-main">
    <div>
      <p>お見積り・ご質問等は<br>こちらまでお気軽にお問い合わせ下さい。</p>
      <div class="tel">TEL 083-000-4817</div>
      <p class="address">〒759-0000 山口県下関市椎野町5-7-3</p>
    </div>
  </div>
</section>

</body>
</html>
```